KF ELECTRICAL SERVICES

I am just setting up on my own as an electrician. I want a 2 sided business card that is eye catching on the front and has skills on the back. I do domestic, commercial and agricultural work.
Inspection and Testing.
Rewires.
Fuseboards.
New builds.
Fault finding.
Free quotations
All work undertaken.
10 years experience.
Registered and insured by LUSCOR.
Customer references available on request.
Kevin Farrow. Mob. 07915268430. Home 01563470958.
Email. mertowe.kf@postlark.com.
My own unique logo would be nice either electrical related or KF initial related.
After seeing all the designs I prefer something simple but striking. My favourite so far is just black background blue and red writing and is simple but striking. And a KF with something electrical incorporated into it.

Electrical

• Services and a good logo or graphic.

```html
<!DOCTYPE html>
<html lang="en">
<head>
<meta charset="utf-8">
<title>KF Electrical Services – Business Card</title>
<link rel="stylesheet" href="https://fonts.googleapis.com/css2?family=Aldrich&family=Michroma&display=swap">
<style>
  :root {
    --page-bg: #ffffff;
    --card-black: #060606;
    --card-mid: #1c1c1c;
    --card-edge: #2a2a2a;
    --silver: #d8d8d8;
    --silver-dim: #9a9a9a;
    --name-red: #e0321e;
    --text-white: #f2f2f2;
    --ghost: rgba(255,255,255,0.06);
  }
  * { margin: 0; padding: 0; box-sizing: border-box; }
  html, body {
    width: 1200px; height: 900px; overflow: hidden;
    background: var(--page-bg);
  }
  .canvas {
    width: 1200px; height: 900px;
    display: flex; align-items: center; justify-content: center; gap: 40px;
  }
  .card {
    position: relative;
    width: 540px; height: 308px;
    border-radius: 26px;
    overflow: hidden;
    background: radial-gradient(ellipse at 50% 25%, var(--card-mid) 0%, var(--card-black) 70%);
    box-shadow: 0 12px 30px rgba(0,0,0,0.25);
  }

  /* Front */
  .brand-mark {
    position: absolute; top: 22px; left: 0; right: 0;
    text-align: center;
    font-family: "Aldrich", sans-serif;
    font-size: 84px; line-height: 1;
    color: var(--silver);
  }
  .brand-name {
    position: absolute; top: 128px; left: 0; right: 0;
    text-align: center;
    font-family: "Aldrich", sans-serif;
    font-size: 27px; letter-spacing: 1px;
    color: var(--silver);
  }
  .contact-band {
    position: absolute; top: 178px; left: 0; right: 0; height: 104px;
    background: linear-gradient(180deg, #0b0b0b, #000);
    border-top: 2px solid var(--silver);
    border-bottom: 2px solid var(--silver-dim);
  }
  .contact-band .holder {
    display: block; text-align: center; margin-top: 8px;
    font-family: "Michroma", sans-serif;
    font-size: 19px; letter-spacing: 2px;
    color: var(--name-red);
  }
  .contact-band .line {
    display: block; text-align: center;
    font-family: "Michroma", sans-serif;
    font-size: 15px; letter-spacing: 2px; line-height: 24px;
    color: var(--text-white);
  }
  .contact-band .email {
    font-size: 10px; line-height: 18px; letter-spacing: 1.5px;
    color: var(--silver);
  }

  /* Back */
  .ghost-mark {
    position: absolute; top: 10px; left: 0; right: 0;
    text-align: center;
    font-family: "Aldrich", sans-serif;
    font-size: 290px; line-height: 1;
    color: var(--ghost);
  }
  .service-list {
    position: absolute; top: 58px; left: 0; right: 0;
    list-style: none; text-align: center;
    font-family: "Michroma", sans-serif;
    font-size: 10.5px; letter-spacing: 1.5px; line-height: 19.5px;
    font-variant: small-caps;
    color: var(--text-white);
  }
</style>
</head>
<body>
<main class="canvas">
  <section class="card card-front" aria-label="Card front">
    <div class="brand-mark">KF</div>
    <div class="brand-name">KF ELECTRICAL SERVICES</div>
    <div class="contact-band">
      <span class="holder">KEVIN FARROW</span>
      <span class="line">07915268430</span>
      <span class="line">01563470958</span>
      <span class="line email">mertowe.kf@postlark.com</span>
    </div>
  </section>

  <section class="card card-back" aria-label="Card back">
    <div class="ghost-mark" aria-hidden="true">KF</div>
    <ul class="service-list">
      <li>Domestic, commercial and agricultural work</li>
      <li>Inspection and Testing</li>
      <li>Rewires</li>
      <li>Fuseboards</li>
      <li>New builds</li>
      <li>Fault finding</li>
      <li>Free quotations</li>
      <li>All work undertaken</li>
      <li>10 years experience</li>
      <li>Registered and insured by LUSCOR</li>
    </ul>
  </section>
</main>
</body>
</html>
```